Stationery Design Project

We are looking stationary Design for Velbrin Global, a high end clothing company. I have attached an image of our Logo below.
Updates
I am looking for designs for the following stationaries:
1. Leather Binders
2. Paper Binders
3. Letterhead
4. Envelopes
5. Pens, pencils etc
We would love to see designs with gold, black and white color combination.
Industry/Entity Type
Clothing
Look and feel
Each slider illustrates characteristics of the customer's brand and the style your logo design should communicate.

```html
<!DOCTYPE html>
<html lang="en">
<head>
<meta charset="utf-8">
<title>Velbrin Global Stationery</title>
<link href="https://fonts.googleapis.com/css2?family=Cinzel:wght@500&display=swap" rel="stylesheet">
<style>
  :root {
    --black: #0b0b0b;
    --white: #ffffff;
    --gold: #c9a93a;
    --backdrop: #e4e4e4;
    --divider: #ffffff;
    --shadow: 0 6px 18px rgba(0,0,0,0.25);
  }
  * { margin: 0; padding: 0; box-sizing: border-box; }
  html, body { width: 1200px; height: 467px; overflow: hidden; background: var(--divider); }
  .canvas { position: relative; width: 1200px; height: 467px; }
  .panel { position: absolute; background: var(--backdrop); overflow: hidden; }
  .panel--box { left: 0; top: 0; width: 548px; height: 230px; }
  .panel--binder { left: 0; top: 235px; width: 548px; height: 232px; }
  .panel--suite { left: 553px; top: 0; width: 647px; height: 467px; }

  .brand {
    font-family: "Cinzel", serif;
    font-weight: 500;
    color: var(--gold);
    text-align: center;
    line-height: 1.15;
    letter-spacing: 0.12em;
    text-transform: uppercase;
    white-space: nowrap;
  }
  .brand-dot {
    display: block; margin: 0 auto 4px;
    border: 1px solid var(--gold); border-radius: 50%;
  }

  /* Box lid */
  .box-lid {
    position: absolute; left: 164px; top: 30px; width: 220px; height: 170px;
    background: var(--white); box-shadow: var(--shadow);
  }
  .box-lid .brand-block { position: absolute; left: 0; right: 0; top: 22px; }
  .box-lid .brand { font-size: 12px; }
  .box-lid .brand-dot { width: 22px; height: 22px; }
  .box-lid__band {
    position: absolute; left: 0; right: 0; top: 104px; height: 30px;
    background: var(--black); border-bottom: 2px solid var(--gold);
  }

  /* Binder cover */
  .binder {
    position: absolute; left: 199px; top: 20px; width: 150px; height: 192px;
    background: var(--black); box-shadow: var(--shadow); border-left: 4px solid #1c1c1c;
  }
  .binder__rule {
    position: absolute; left: 26px; right: 26px; height: 1px;
    background: linear-gradient(90deg, transparent, var(--gold), transparent);
  }
  .binder__rule--top { top: 30px; }
  .binder__rule--bottom { bottom: 30px; }
  .binder .brand-block { position: absolute; left: 0; right: 0; top: 62px; }
  .binder .brand { font-size: 13px; }
  .binder .brand-dot { width: 26px; height: 26px; }

  /* Letterhead */
  .letterhead {
    position: absolute; left: 50px; top: 60px; width: 240px; height: 330px;
    background: var(--white); box-shadow: var(--shadow);
  }
  .letterhead__band {
    position: absolute; left: 0; top: 0; bottom: 0; width: 44px;
    background: var(--black); border-right: 2px solid var(--gold);
  }
  .letterhead .brand-block { position: absolute; left: 0; width: 44px; top: 10px; }
  .letterhead .brand { font-size: 5px; letter-spacing: 0.06em; }
  .letterhead .brand-dot { width: 10px; height: 10px; margin-bottom: 2px; }

  /* Envelopes */
  .envelope {
    position: absolute; left: 345px; width: 260px; height: 92px; box-shadow: var(--shadow);
  }
  .envelope--white-back { top: 30px; background: var(--white); }
  .envelope--white-front { top: 132px; background: var(--white); }
  .envelope--black-back { top: 240px; background: var(--black); }
  .envelope--black-front { top: 342px; background: var(--black); }
  .envelope__flap { position: absolute; inset: 0; width: 100%; height: 100%; }
  .envelope__band {
    position: absolute; right: 0; top: 0; bottom: 0; width: 52px;
  }
  .envelope--white-front .envelope__band { background: var(--black); border-left: 2px solid var(--gold); }
  .envelope--black-front .envelope__band { background: var(--white); border-left: 2px solid var(--gold); }
  .envelope .brand-block { position: absolute; right: 0; width: 52px; bottom: 10px; }
  .envelope .brand { font-size: 5px; letter-spacing: 0.06em; }
  .envelope .brand-dot { width: 10px; height: 10px; margin-bottom: 2px; }
</style>
</head>
<body>
<main class="canvas">

  <section class="panel panel--box" aria-label="Gift box lid">
    <div class="box-lid">
      <div class="brand-block">
        <span class="brand-dot"></span>
        <p class="brand">Velbrin<br>Global</p>
      </div>
      <div class="box-lid__band"></div>
    </div>
  </section>

  <section class="panel panel--binder" aria-label="Binder cover">
    <div class="binder">
      <div class="binder__rule binder__rule--top"></div>
      <div class="brand-block">
        <span class="brand-dot"></span>
        <p class="brand">Velbrin<br>Global</p>
      </div>
      <div class="binder__rule binder__rule--bottom"></div>
    </div>
  </section>

  <section class="panel panel--suite" aria-label="Letterhead and envelopes">
    <div class="letterhead">
      <div class="letterhead__band"></div>
      <div class="brand-block">
        <span class="brand-dot"></span>
        <p class="brand">Velbrin<br>Global</p>
      </div>
    </div>

    <div class="envelope envelope--white-back">
      <svg class="envelope__flap" viewBox="0 0 260 92" preserveAspectRatio="none">
        <polygon points="0,0 260,0 130,48" fill="#f4f4f4" stroke="#d6d6d6" stroke-width="1"/>
        <polygon points="215,0 260,0 260,30" fill="var(--black)"/>
        <line x1="215" y1="0" x2="260" y2="30" stroke="var(--gold)" stroke-width="1.5"/>
      </svg>
    </div>

    <div class="envelope envelope--white-front">
      <div class="envelope__band"></div>
      <div class="brand-block">
        <span class="brand-dot"></span>
        <p class="brand">Velbrin<br>Global</p>
      </div>
    </div>

    <div class="envelope envelope--black-back">
      <svg class="envelope__flap" viewBox="0 0 260 92" preserveAspectRatio="none">
        <polygon points="0,0 260,0 130,48" fill="#151515" stroke="#2a2a2a" stroke-width="1"/>
        <polygon points="215,0 260,0 260,30" fill="var(--white)"/>
        <line x1="215" y1="0" x2="260" y2="30" stroke="var(--gold)" stroke-width="1.5"/>
      </svg>
    </div>

    <div class="envelope envelope--black-front">
      <div class="envelope__band"></div>
      <div class="brand-block">
        <span class="brand-dot"></span>
        <p class="brand">Velbrin<br>Global</p>
      </div>
    </div>
  </section>

</main>
</body>
</html>
```